Corvend Utility Services Ltd. -Website Design

We need a site design for a new company based in Toronto, Ontario called 'Corvend Utility Services Ltd.'

We provide Engineering services, Subsurface Utility Engineering services and Geospatial Data Management.

Our clients are typically Utilities (electric, gas, water/waste water, telcom) or contractors/consultants working on their behalf.

Our business model is new and we are the first to offer all three services to our clients; this allows us to provide value-added services from all three of our main offerings.

Target Market(s)

Field Supervisors, Managers, Directors, VP's at Utility companies

Industry/Entity Type

Business

Requirements
Must have
• -The landing page must clearly identify the 3 main business offerings allowing the user to easily navigate to each....Utility Engineering, GIS Data Management & Sub-surface Utility Engineering (SUE).

-Interactive contact page with integrated email

-based on existing logo design...
Nice to have
• -Ability to easily add/post news releases, updates, jobs, etc...

-Ability to integrate instructional YouTube video(s)

Should not have
• -Cannot be too cluttered....

```html
<!DOCTYPE html>
<html lang="en">
<head>
<meta charset="utf-8">
<title>Corvend Utility Services</title>
<link rel="stylesheet" href="https://fonts.googleapis.com/css2?family=Ubuntu:wght@400;500;700&display=swap">
<style>
:root{
  --dark:#3d3d3d;
  --hero-bg:#eeeeee;
  --band-bg:#dedede;
  --white:#ffffff;
  --blue-top:#42a9cf;
  --blue-bottom:#1d7ca5;
  --blue-text:#1f7fa5;
  --body-grey:#7a7a7a;
  --text-dark:#3a3a3a;
  --line:#d4d4d4;
  --footer-text:#e6e6e6;
  --map-tone:#5c6f7a;
  --dam-tone:#a7a9a6;
  --chart-tone:#e4e1dc;
  --canyon-tone:#b0672c;
  --video-tone:#2a6d83;
}
*{box-sizing:border-box;margin:0;padding:0}
html,body{width:1200px;height:1200px;overflow:hidden}
body{font-family:"Ubuntu",sans-serif;background:var(--white);position:relative}
h1,h2{font-weight:400}
.header{position:absolute;left:0;top:0;width:1200px;height:109px;background:var(--dark)}
.brand{position:absolute;left:121px;top:18px;display:flex;align-items:center;gap:12px}
.brand-mark{width:30px;height:30px;background:var(--blue-top);border-radius:4px}
.brand-name{font-size:28px;font-weight:500;color:var(--white);letter-spacing:2px}
.nav{position:absolute;left:121px;top:71px;width:958px;height:38px;border-radius:6px 6px 0 0;
  background:linear-gradient(var(--blue-top),var(--blue-bottom));display:flex;align-items:stretch}
.nav-home{width:34px;display:flex;align-items:center;justify-content:center;border-right:1px solid rgba(255,255,255,.35)}
.nav-item{padding:0 19px;display:flex;align-items:center;color:var(--white);font-size:14px;border-right:1px solid rgba(255,255,255,.35)}
.nav-search{position:absolute;right:10px;top:8px;width:170px;height:22px;background:var(--white);border-radius:4px;border:1px solid #9ccbe0}
.nav-search svg{position:absolute;right:6px;top:3px}
.hero-band{position:absolute;left:0;top:109px;width:1200px;height:371px;background:var(--hero-bg)}
.hero-shadow{position:absolute;left:170px;top:432px;width:860px;height:30px;border-radius:50%;
  background:radial-gradient(ellipse at center,rgba(0,0,0,.28),rgba(0,0,0,0) 70%)}
.hero-card{position:absolute;left:121px;top:109px;width:958px;height:336px;background:var(--white);border:1px solid var(--line);border-top:none}
.hero-title{position:absolute;left:34px;top:26px;font-size:24px;font-weight:500;color:var(--text-dark)}
.hero-text{position:absolute;left:34px;top:64px;width:565px;font-size:16px;line-height:30px;color:var(--body-grey)}
.btn{background:linear-gradient(var(--blue-top),var(--blue-bottom));color:var(--white);border-radius:5px;display:flex;align-items:center;justify-content:center}
.hero-btn{position:absolute;left:34px;top:266px;width:172px;height:38px;font-size:15px}
.hero-image{position:absolute;left:648px;top:0;width:310px;height:336px;background:linear-gradient(135deg,#6c7f8a,var(--map-tone))}
.services-band{position:absolute;left:0;top:480px;width:1200px;height:297px;background:var(--band-bg);border-bottom:2px solid #f4f4f4}
.service-card{position:absolute;top:19px;width:308px;height:252px;background:var(--white);border-radius:3px}
.service-card::after{content:"";position:absolute;left:14px;right:14px;bottom:-16px;height:14px;border-radius:50%;
  background:radial-gradient(ellipse at center,rgba(0,0,0,.35),rgba(0,0,0,0) 70%)}
.service-title{position:absolute;left:19px;top:20px;font-size:16.5px;font-weight:400;color:var(--blue-text);white-space:nowrap;letter-spacing:-0.2px}
.service-text{position:absolute;left:19px;top:52px;width:265px;font-size:12.5px;line-height:20px;color:var(--text-dark)}
.service-image{position:absolute;left:19px;top:141px;width:270px;height:101px;border:1px solid var(--line)}
.dam{background:linear-gradient(160deg,#cfd1cd,var(--dam-tone))}
.charts{background:linear-gradient(160deg,#f2f0ec,var(--chart-tone))}
.canyon{background:linear-gradient(180deg,#c8813f,var(--canyon-tone) 50%,#4a3422)}
.video-box{position:absolute;left:121px;top:793px;width:634px;height:297px;border:1px solid var(--line);border-radius:3px}
.video-frame{position:absolute;left:10px;top:7px;width:610px;height:284px;background:radial-gradient(ellipse at 50% 45%,#4b93a7,var(--video-tone) 70%)}
.video-controls{position:absolute;left:0;bottom:0;width:100%;height:22px;background:#1b1b1b}
.video-progress{position:absolute;left:0;top:0;width:100%;height:3px;background:#555}
.video-progress span{display:block;width:95px;height:3px;background:#c4302b}
.video-time{position:absolute;left:74px;top:7px;font-size:8px;color:#ddd}
.contact{position:absolute;left:780px;top:793px;width:299px}
.contact-head{display:flex;align-items:center;gap:10px;font-size:20px;font-weight:400;color:var(--blue-text)}
.field-label{font-size:10px;font-weight:500;color:var(--text-dark);margin-top:10px;margin-bottom:7px}
.field{width:299px;height:30px;border:1px solid var(--line);border-radius:4px}
.field.message{height:73px}
.submit{width:82px;height:31px;font-size:12px;font-weight:500;margin-top:11px}
.footer{position:absolute;left:0;top:1107px;width:1200px;height:93px;background:var(--dark);color:var(--footer-text);font-size:11.5px}
.footer-address{position:absolute;left:121px;top:10px;line-height:17px}
.footer-address span{margin-right:14px}
.footer-copy{position:absolute;right:121px;top:10px}
</style>
</head>
<body>
<header class="header">
  <div class="brand"><div class="brand-mark"></div><div class="brand-name">CORVEND</div></div>
  <nav class="nav">
    <div class="nav-home">
      <svg width="16" height="14" viewBox="0 0 16 14"><path d="M8 1 1 7h2v6h4V9h2v4h4V7h2z" fill="#fff"/></svg>
    </div>
    <div class="nav-item">About Us</div>
    <div class="nav-item">News</div>
    <div class="nav-item">Services</div>
    <div class="nav-item">Blog</div>
    <div class="nav-item">Contact Us</div>
    <div class="nav-search">
      <svg width="16" height="14" viewBox="0 0 16 14"><circle cx="6" cy="6" r="4" fill="none" stroke="#1d7ca5" stroke-width="2"/><path d="M9 9l5 4" stroke="#1d7ca5" stroke-width="2.5"/></svg>
    </div>
  </nav>
</header>

<section class="hero-band"></section>
<div class="hero-shadow"></div>
<section class="hero-card">
  <h1 class="hero-title">Lorem Ipsum Dolor</h1>
  <p class="hero-text">Lorem ipsum dolor sit amet, consectetuer adipiscing elit. Nam cursus. Morbi ut mi. Nullam enim leo, egestas id, condimentum at, laoreet mattis, massa. Sed eleifend nonummy diam. Praesent mauris ante, elementum et, bibendum at, posuere sit amet, nibh. Duis tincidunt lectus quis dui viverra vestibulum. Suspendisse vulputate aliquam dui. Nulla elementum dui ut augue. Aliquam vehicula mi at mauris.</p>
  <div class="btn hero-btn">Learn More</div>
  <div class="hero-image" role="img" aria-label="Engineering site plan drawing with utility lines"></div>
</section>

<section class="services-band">
  <article class="service-card" style="left:121px">
    <h2 class="service-title">Utility Engineering</h2>
    <p class="service-text">Lorem ipsum dolor sit amet, consectetur adipisicing elit, sed do eiusmod tempor incididunt ut labore et dolore magna aliqua. Ut enim ad minim veniam.</p>
    <div class="service-image dam" role="img" aria-label="Hydroelectric dam in winter"></div>
  </article>
  <article class="service-card" style="left:446px">
    <h2 class="service-title">GIS Data Management</h2>
    <p class="service-text">Lorem ipsum dolor sit amet, consectetur adipisicing elit, sed do eiusmod tempor incididunt ut labore et dolore magna aliqua. Ut enim ad minim veniam.</p>
    <div class="service-image charts" role="img" aria-label="Printed data reports with charts"></div>
  </article>
  <article class="service-card" style="left:771px">
    <h2 class="service-title">Sub-surface Utility Engineering (SUE)</h2>
    <p class="service-text">Lorem ipsum dolor sit amet, consectetur adipisicing elit, sed do eiusmod tempor incididunt ut labore et dolore magna aliqua. Ut enim ad minim veniam.</p>
    <div class="service-image canyon" role="img" aria-label="Dam wall beside a canyon at sunset"></div>
  </article>
</section>

<section class="video-box">
  <div class="video-frame" role="img" aria-label="Video still of a quality word cloud">
    <svg style="position:absolute;left:289px;top:118px" width="28" height="32" viewBox="0 0 28 32"><path d="M2 2v28l24-14z" fill="rgba(0,0,0,.7)"/></svg>
    <div class="video-controls">
      <div class="video-progress"><span></span></div>
      <svg style="position:absolute;left:14px;top:7px" width="40" height="10" viewBox="0 0 40 10"><rect x="0" y="0" width="3" height="10" fill="#ddd"/><rect x="6" y="0" width="3" height="10" fill="#ddd"/><path d="M26 3h3l4-3v10l-4-3h-3z" fill="#ddd"/></svg>
      <div class="video-time">0:18 / 1:34</div>
      <svg style="position:absolute;right:12px;top:6px" width="64" height="11" viewBox="0 0 64 11"><circle cx="5" cy="5.5" r="4" fill="none" stroke="#ddd" stroke-width="2.5" stroke-dasharray="2 1.2"/><circle cx="29" cy="5.5" r="4.5" fill="#ddd"/><path d="M52 4V1h3M61 1h3v3M64 7v3h-3M55 10h-3V7" fill="none" stroke="#ddd" stroke-width="1.5"/></svg>
    </div>
  </div>
</section>

<section class="contact">
  <h2 class="contact-head">
    <svg width="30" height="28" viewBox="0 0 30 28"><rect x="2" y="8" width="22" height="17" fill="#fff" stroke="#888"/><path d="M2 8l11 9 11-9" fill="none" stroke="#888"/><path d="M10 18 25 3l3 3-15 15-4 1z" fill="#e8a33a" stroke="#9a5f14"/></svg>
    Get in touch with us:
  </h2>
  <div class="field-label">NAME:</div>
  <div class="field"></div>
  <div class="field-label">E-MAIL:</div>
  <div class="field"></div>
  <div class="field-label">MESSAGE:</div>
  <div class="field message"></div>
  <div class="btn submit">SUBMIT</div>
</section>

<footer class="footer">
  <div class="footer-address">
    118-4 Alder Ridge Rd, Toronto, ON M4B 2K7<br>
    <span>T - 416.555.0142</span><span>F - 416.555.0143</span><span>E - info@corvend.ca</span>
  </div>
  <div class="footer-copy">© 2012 Corvend.ca. All Rights Reserved.</div>
</footer>
</body>
</html>
```